Business cards for a naturopathic day clinic for stem cell therapy

We need a basic design for a day clinic, that offers stem cell therapies for Lyme therapy and other severe chronic illnesses.
Our name is "Casa velorìn", which can be translated into "Manor Velorbloom". We are a couple of naturopaths working along side physiotherapists and osteopaths, yoga teachers and massage therapists. I attached our logo.

```html
<!DOCTYPE html>
<html lang="en">
<head>
<meta charset="utf-8">
<title>Casa velorìn – Business Cards</title>
<link href="https://fonts.googleapis.com/css2?family=Nunito:wght@400;600;800&family=Quicksand:wght@300&display=swap" rel="stylesheet">
<style>
  :root{
    --backdrop:#9ea096;
    --paper:#f4f4f2;
    --sage:#e3e7db;
    --taupe:#85736a;
    --leaf:#8db043;
    --gold-light:#b08f3a;
    --gold-dark:#7d6420;
    --ink:#1e1e1e;
  }
  html,body{margin:0;padding:0;}
  body{
    width:1200px;height:1000px;overflow:hidden;
    background:var(--backdrop);
    position:relative;
    font-family:"Nunito",sans-serif;
  }
  .card{
    position:absolute;left:200px;width:800px;height:457px;
    border-radius:6px;overflow:hidden;
    box-shadow:0 10px 30px rgba(0,0,0,.18);
  }
  .card svg.card-art{position:absolute;inset:0;width:100%;height:100%;}
  .card--front{top:36px;background:var(--paper);}
  .card--back{top:515px;background:var(--sage);}

  /* Front */
  .front-brand{
    position:absolute;left:120px;top:182px;
    display:flex;align-items:center;gap:26px;
  }
  .brand-dot{
    width:84px;height:84px;border-radius:50%;
    background:var(--leaf);
  }
  .brand-name{
    font-family:"Quicksand",sans-serif;font-weight:300;
    font-size:70px;color:var(--taupe);letter-spacing:1px;
    line-height:1;
  }

  /* Back */
  .back-title{
    position:absolute;left:300px;top:98px;
    font-weight:800;font-size:40px;letter-spacing:2px;
    color:var(--taupe);margin:0;
  }
  .contact-list{
    position:absolute;left:60px;top:190px;
    list-style:none;margin:0;padding:0 0 0 26px;
    border-left:3px solid var(--leaf);
  }
  .contact-list li{
    position:relative;
    font-size:25px;font-weight:600;color:var(--ink);
    line-height:44px;
  }
  .contact-list .icon{
    position:absolute;left:-62px;top:12px;width:20px;height:20px;
  }
  .seal{
    position:absolute;right:70px;bottom:50px;
    width:110px;height:110px;border-radius:50%;
    background:linear-gradient(135deg,var(--gold-light),var(--gold-dark));
  }
</style>
</head>
<body>

<section class="card card--front" aria-label="Business card front">
  <svg class="card-art" viewBox="0 0 800 457" preserveAspectRatio="none">
    <path d="M0 0 H800 V20 C620 40 520 150 380 130 C250 112 170 60 0 140 Z" fill="var(--taupe)"/>
    <defs>
      <linearGradient id="gold-band" x1="0" y1="0" x2="1" y2="1">
        <stop offset="0" stop-color="#a88a38"/>
        <stop offset="0.5" stop-color="#8a6f26"/>
        <stop offset="1" stop-color="#a2843a"/>
      </linearGradient>
    </defs>
    <path role="img" aria-label="Gold foil wave band" d="M0 457 C120 430 220 360 330 345 C470 325 560 380 640 300 C700 240 740 200 800 190 V457 Z" fill="url(#gold-band)"/>
  </svg>
  <div class="front-brand">
    <span class="brand-dot"></span>
    <span class="brand-name">Casa velorìn</span>
  </div>
</section>

<section class="card card--back" aria-label="Business card back">
  <svg class="card-art" viewBox="0 0 800 457" preserveAspectRatio="none">
    <path d="M470 0 H800 V457 H775 C770 250 680 80 470 0 Z" fill="var(--paper)"/>
    <path d="M0 8 C250 -5 520 10 700 120 C760 160 785 250 790 457" fill="none" stroke="var(--taupe)" stroke-width="3"/>
    <g fill="var(--leaf)">
      <circle cx="300" cy="158" r="4"/><circle cx="318" cy="158" r="4"/><circle cx="336" cy="158" r="4"/>
      <circle cx="354" cy="158" r="4"/><circle cx="372" cy="158" r="4"/><circle cx="390" cy="158" r="4"/>
      <circle cx="408" cy="158" r="4"/><circle cx="426" cy="158" r="4"/><circle cx="444" cy="158" r="4"/>
      <circle cx="462" cy="158" r="4"/><circle cx="480" cy="158" r="4"/><circle cx="498" cy="158" r="4"/>
      <circle cx="516" cy="158" r="4"/><circle cx="534" cy="158" r="4"/><circle cx="552" cy="158" r="4"/>
      <circle cx="570" cy="158" r="4"/><circle cx="588" cy="158" r="4"/><circle cx="606" cy="158" r="4"/>
      <circle cx="624" cy="158" r="4"/><circle cx="642" cy="158" r="4"/>
    </g>
  </svg>

  <h2 class="back-title">CASA VELORÌN</h2>

  <ul class="contact-list">
    <li>
      <svg class="icon" viewBox="0 0 20 20"><path d="M5 2 L8 6 L6 8 C7 11 9 13 12 14 L14 12 L18 15 L16 18 C9 18 2 11 2 4 Z" fill="var(--taupe)"/></svg>
      +49 6100 5550142
    </li>
    <li>
      <svg class="icon" viewBox="0 0 20 20"><rect x="2" y="4" width="16" height="12" fill="var(--taupe)"/><path d="M2 4 L10 11 L18 4" fill="none" stroke="#fff" stroke-width="1.5"/></svg>
      info@casa-velorin.de
    </li>
    <li>
      <svg class="icon" viewBox="0 0 20 20"><path d="M3 3 L17 9 L11 11 L9 17 Z" fill="var(--taupe)"/></svg>
      www.casa-velorin.de
    </li>
    <li>
      <svg class="icon" viewBox="0 0 20 20"><path d="M10 1 C6 1 4 4 4 7 C4 11 10 19 10 19 C10 19 16 11 16 7 C16 4 14 1 10 1 Z" fill="var(--taupe)"/><circle cx="10" cy="7" r="2.2" fill="#fff"/></svg>
      Lindenweg 8, 64800 Talheim, Germany
    </li>
  </ul>

  <span class="seal" aria-hidden="true"></span>
</section>

</body>
</html>
```